Book cover for LM

Design cover for a book of gratitude and inspiration.
Book trim size will be 6.5 x 6.5 inches, or 8 x 8 inches, hardcover, 96 pages
Title: Lantern Meadows
Subtitle: A Book of Gratitude and Inspiration
Author: Gus Halverd

```html
<!DOCTYPE html>
<html lang="en">
<head>
<meta charset="utf-8">
<title>Lantern Meadows – Book Cover Spread</title>
<link rel="stylesheet" href="https://fonts.googleapis.com/css2?family=Cinzel:wght@400;600;700&family=Montserrat:wght@400;600&display=swap">
<style>
  :root {
    --page-bg: #ebebeb;
    --back-blue: #4280aa;
    --spine-dark: #3c78a3;
    --spine-light: #5d9ec8;
    --title-white: #ffffff;
    --ink: #0c0c0c;
    --copy-white: #f4f8fb;
    --rule-green: #93c98c;
    --photo-grey: #e4e4e4;
    --photo-line: #9a9a9a;
    --code-box: #ffffff;
  }
  * { margin: 0; padding: 0; box-sizing: border-box; }
  html, body { width: 1200px; height: 1200px; overflow: hidden; background: var(--page-bg); }
  .spread {
    position: absolute;
    left: 72px; top: 343.5px;
    width: 1056px; height: 511.5px;
    filter: drop-shadow(0 6px 10px rgba(0,0,0,0.28));
  }
  .spread-art { position: absolute; inset: 0; display: block; }
  .title-face { font-family: "Cinzel", "Times New Roman", serif; }
  .back-copy {
    position: absolute;
    left: 61.5px; top: 160px;
    width: 390px;
    font-family: "Montserrat", Arial, sans-serif;
    font-size: 7.7px;
    line-height: 12.9px;
    color: var(--copy-white);
    text-align: justify;
  }
  .back-copy p + p { margin-top: 3.5px; }
  .back-rule {
    position: absolute;
    left: 61px; top: 358.5px;
    width: 392px; height: 2.5px;
    background: var(--rule-green);
  }
  .author-photo {
    position: absolute;
    left: 60px; top: 367.5px;
    width: 53px; height: 61.5px;
    background: var(--photo-grey);
    border: 1px solid var(--photo-line);
  }
  .author-photo svg { width: 100%; height: 100%; display: block; }
  .author-bio {
    position: absolute;
    left: 120.5px; top: 366px;
    width: 326px;
    font-family: "Montserrat", Arial, sans-serif;
    font-size: 7.6px;
    line-height: 10.9px;
    color: var(--copy-white);
    text-align: justify;
  }
  .author-bio strong { font-weight: 600; }
  .bio-spacer { float: right; width: 0; height: 44px; }
  .code-box {
    float: right; clear: right;
    width: 100px; height: 59.5px;
    margin-right: -23px; margin-left: 6px;
    background: var(--code-box);
  }
</style>
</head>
<body>
<div class="spread">
  <svg class="spread-art" width="1056" height="511.5" viewBox="0 0 1056 511.5" xmlns="http://www.w3.org/2000/svg">
    <defs>
      <linearGradient id="spineShade" x1="0" y1="0" x2="1" y2="0">
        <stop offset="0" stop-color="var(--spine-dark)"/>
        <stop offset="0.25" stop-color="#3a74a0"/>
        <stop offset="1" stop-color="var(--spine-light)"/>
      </linearGradient>
      <linearGradient id="frontWash" x1="0" y1="0" x2="1" y2="0">
        <stop offset="0" stop-color="#4d90bf"/>
        <stop offset="0.3" stop-color="#9fd4ee"/>
        <stop offset="0.7" stop-color="#dcf2fb"/>
        <stop offset="1" stop-color="#eaf8fd"/>
      </linearGradient>
      <radialGradient id="frontGlow" cx="0.62" cy="0.52" r="0.55">
        <stop offset="0" stop-color="#ffffff" stop-opacity="0.95"/>
        <stop offset="0.5" stop-color="#eaf8fd" stop-opacity="0.6"/>
        <stop offset="1" stop-color="#eaf8fd" stop-opacity="0"/>
      </radialGradient>
    </defs>

    <!-- back cover -->
    <rect class="back-cover" x="0" y="0" width="502.5" height="511.5" fill="var(--back-blue)"/>
    <g class="title-face back-title" fill="var(--title-white)" style="filter: drop-shadow(1px 1px 0.6px rgba(0,0,0,0.55))">
      <text x="99" y="78" font-size="52" font-weight="600" textLength="312.75" lengthAdjust="spacing">LANTERN</text>
      <text x="98" y="126.75" font-size="60" font-weight="600" textLength="315" lengthAdjust="spacingAndGlyphs">MEADOWS</text>
      <text x="97.5" y="147.75" font-size="19" textLength="310.5" lengthAdjust="spacingAndGlyphs">A Book of Gratitude and Inspiration</text>
    </g>

    <!-- spine -->
    <rect class="spine" x="502.5" y="0" width="48.75" height="511.5" fill="url(#spineShade)"/>
    <g class="title-face spine-text" fill="var(--ink)">
      <text transform="translate(519.5 39) rotate(90)" font-size="21" textLength="296" lengthAdjust="spacing">LANTERN MEADOWS</text>
      <text transform="translate(519.5 354) rotate(90)" font-size="21" textLength="121.5" lengthAdjust="spacingAndGlyphs">GUS HALVERD</text>
    </g>

    <!-- front cover -->
    <g class="front-image" role="img" aria-label="Cover photograph: a blue chess pawn casting a long shadow shaped like a king across a pale blue glow">
      <rect x="551.25" y="0" width="504.75" height="511.5" fill="url(#frontWash)"/>
      <rect x="551.25" y="0" width="504.75" height="511.5" fill="url(#frontGlow)"/>
    </g>
    <g class="title-face front-title" fill="var(--ink)">
      <text x="588" y="76.5" font-size="66" font-weight="600" textLength="425" lengthAdjust="spacing">LANTERN</text>
      <text x="588" y="144" font-size="82" font-weight="600" textLength="425.25" lengthAdjust="spacingAndGlyphs">MEADOWS</text>
      <text x="588" y="168" font-size="25" textLength="425.25" lengthAdjust="spacingAndGlyphs">A Book of Gratitude and Inspiration</text>
      <text x="801" y="475.5" font-size="37" font-weight="600" text-anchor="middle" textLength="228" lengthAdjust="spacingAndGlyphs">GUS HALVERD</text>
    </g>
  </svg>

  <div class="back-copy">
    <p>Some days arrive quietly and ask for nothing more than our attention. This small book gathers short sayings, gentle reminders and simple reflections meant to be read slowly, one page at a time. Each entry invites you to pause, notice what is already good, and carry that sense of thanks into the hours ahead. Keep it near a window, a bedside or a kitchen table, and open it whenever the world feels loud or heavy. Let the words settle like lantern light across a meadow in the early evening, warm and steady, asking nothing, simply showing the way home again.</p>
    <p>Gratitude is not a single feeling but a practice that grows with care. These pages pair timeless proverbs with fresh thoughts on kindness, patience, hope and courage. Read them alone or share them with a friend, a child or a neighbour who could use a lift. Mark the lines that speak to you, return to them often, and watch how small moments of thanks begin to bloom into a fuller, brighter way of living. Whether you read one page each morning or the whole book in a quiet afternoon, may it remind you that there is always something worth noticing, something worth keeping, and someone worth thanking today.</p>
  </div>

  <div class="back-rule"></div>

  <div class="author-photo" role="img" aria-label="Author portrait placeholder">
    <svg viewBox="0 0 53 61.5" preserveAspectRatio="none">
      <line x1="0" y1="0" x2="53" y2="61.5" stroke="var(--photo-line)" stroke-width="0.8"/>
      <line x1="53" y1="0" x2="0" y2="61.5" stroke="var(--photo-line)" stroke-width="0.8"/>
    </svg>
  </div>

  <div class="author-bio">
    <span class="bio-spacer"></span>
    <span class="code-box"></span>
    <strong>About the Author:</strong> Gus Halverd writes short reflections on everyday thankfulness and the quiet lessons found in ordinary days. He lives near the coast with his family, where he walks each morning, keeps a small garden and collects old sayings from friends and strangers alike. His notes have been shared in newsletters, classrooms and kitchens for many years, always with one hope: that readers pause and give thanks.
  </div>
</div>
</body>
</html>
```